K7 Digital Stationery Design Project

We are looking to have stationary designs created for our company branding materials. We are looking for the following to be created.
1. Business Cards (front & back)
2. Letterhead
3. Envelopes #10
We are a new web design, development and marketing firm. Primary color scheme is desired to be blue/grey/white. This web start-up is owned and operated by individuals with 15+ years experience each in the industry so should not look as though it is a start-up by young/inexperienced individuals.
We build website & custom applications/software. In addition we provide the full spectrum of web marketing solutions including SEO, PPC, Social Media, Branding, Content Marketing and PR.
Please let us know if you have any questions. Looking forward to seeing all the amazing design ideas.
Attached is our logo.
Thanks!
Target Market(s)
Company will be nearly 100% business to business sales. Looking to work with companies that are already established, with a website, who want to take their website and/or online marketing efforts to the next level.
Industry/Entity Type
Marketing
Look and feel

```html
<!DOCTYPE html>
<html lang="en">
<head>
<meta charset="utf-8">
<title>K7 Digital — Business Card</title>
<link href="https://fonts.googleapis.com/css2?family=Jost:wght@400;500;600;700&display=swap" rel="stylesheet">
<style>
  :root{
    --page:#e6e8eb;
    --blue-deep:#0a6cb8;
    --blue-mid:#1b8fd6;
    --blue-light:#3fb8e8;
    --charcoal:#3b3d40;
    --charcoal-dark:#2a2b2d;
    --silver:#b9bdc2;
    --paper:#f7f7f7;
    --ink:#333638;
    --name:#0d6fb8;
    --white:#ffffff;
  }
  *{margin:0;padding:0;box-sizing:border-box}
  html,body{width:1200px;height:900px;overflow:hidden}
  body{background:var(--page);font-family:"Jost",sans-serif;position:relative}
  .card{position:absolute;left:280px;width:640px;height:366px;overflow:hidden;
        box-shadow:0 6px 18px rgba(0,0,0,.18)}
  .card--back{top:64px}
  .card--front{top:470px;background:var(--paper)}
  .card__art{position:absolute;inset:0;width:100%;height:100%}

  .brand{position:absolute;text-align:center}
  .brand__mark{display:block;width:22px;height:22px;border-radius:50%;margin:0 auto 6px}
  .brand__name{font-weight:700;font-size:28px;letter-spacing:.5px;line-height:1}
  .brand__tag{font-weight:500;font-size:11px;margin-top:4px;letter-spacing:.2px}

  .card--back .brand{right:70px;top:62px;color:var(--white)}
  .card--back .brand__mark{background:var(--white)}
  .card--back .web{position:absolute;left:34px;bottom:30px;color:#d8dadc;font-size:15px}
  .web b{font-weight:600}

  .card--front .brand{right:48px;top:40px;color:var(--ink)}
  .card--front .brand__mark{background:var(--blue-mid)}
  .person{position:absolute;left:38px;top:110px}
  .person__name{color:var(--name);font-weight:500;font-size:24px}
  .person__role{color:var(--ink);font-size:15px;margin-top:2px}
  .contact{position:absolute;left:38px;top:252px;color:var(--white);font-size:14px;line-height:1.3}
  .contact__address{font-weight:600;margin-bottom:10px}
  .contact__row{display:flex;align-items:center;gap:8px}
  .contact__row svg{width:14px;height:14px;fill:var(--white)}
  .card--front .web{position:absolute;right:34px;top:226px;color:var(--white);font-size:14px}
</style>
</head>
<body>

<section class="card card--back" aria-label="Business card back">
  <svg class="card__art" viewBox="0 0 640 366" preserveAspectRatio="none">
    <defs>
      <linearGradient id="backBlue" x1="0" y1="0" x2="1" y2="1">
        <stop offset="0" stop-color="var(--blue-mid)"/>
        <stop offset=".5" stop-color="var(--blue-light)"/>
        <stop offset="1" stop-color="var(--blue-deep)"/>
      </linearGradient>
      <linearGradient id="backGrey" x1="0" y1="1" x2="1" y2="0">
        <stop offset="0" stop-color="var(--charcoal-dark)"/>
        <stop offset="1" stop-color="var(--charcoal)"/>
      </linearGradient>
    </defs>
    <rect width="640" height="366" fill="url(#backBlue)"/>
    <path d="M0,262 C170,300 360,215 640,150 L640,366 L0,366Z" fill="var(--silver)"/>
    <path d="M0,272 C170,312 360,228 640,164 L640,366 L0,366Z" fill="var(--blue-light)"/>
    <path d="M0,286 C160,326 370,240 640,176 L640,366 L0,366Z" fill="url(#backGrey)"/>
  </svg>
  <div class="brand">
    <span class="brand__mark"></span>
    <div class="brand__name">K7 DIGITAL</div>
    <div class="brand__tag">Web Design, Development and Marketing</div>
  </div>
  <p class="web">www.<b>k7digital</b>.com</p>
</section>

<section class="card card--front" aria-label="Business card front">
  <svg class="card__art" viewBox="0 0 640 366" preserveAspectRatio="none">
    <defs>
      <linearGradient id="frontBlue" x1="0" y1="1" x2="1" y2="0">
        <stop offset="0" stop-color="var(--blue-deep)"/>
        <stop offset=".45" stop-color="var(--blue-light)"/>
        <stop offset="1" stop-color="var(--blue-deep)"/>
      </linearGradient>
    </defs>
    <path d="M330,196 C450,190 560,170 640,120 L640,150 C560,186 450,198 330,196Z" fill="var(--blue-light)"/>
    <path d="M0,226 C200,180 420,206 640,158 L640,366 L0,366Z" fill="var(--silver)"/>
    <path d="M0,236 C200,192 420,216 640,170 L640,366 L0,366Z" fill="var(--white)"/>
    <path d="M0,242 C200,200 420,222 640,176 L640,366 L0,366Z" fill="url(#frontBlue)"/>
  </svg>
  <div class="brand">
    <span class="brand__mark"></span>
    <div class="brand__name">K7 DIGITAL</div>
    <div class="brand__tag">Web Design, Development and Marketing</div>
  </div>
  <div class="person">
    <h1 class="person__name">Daniel Mercer</h1>
    <p class="person__role">Position</p>
  </div>
  <p class="web">www.<b>k7digital</b>.com</p>
  <div class="contact">
    <p class="contact__address">1580 W. Harlan Court<br>Lincoln, NE 68502</p>
    <p class="contact__row">
      <svg viewBox="0 0 16 16" aria-hidden="true"><path d="M2 4c0-1 1-2 2-2h8c1 0 2 1 2 2v1h-3V4H5v1H2zM4 6h8l2 7H2z"/></svg>
      +12 3 555-0147
    </p>
    <p class="contact__row">
      <svg viewBox="0 0 16 16" aria-hidden="true"><path d="M1 3h14v10H1zM2 4.5V12h12V4.5L8 9z"/></svg>
      info@k7digital.com
    </p>
  </div>
</section>

</body>
</html>
```